Buisness Card Sationary
Les Sentiers Bleus
Karim BELLAHCENE
Directeur Générale
Centre Commercial et d’Affaire Ennakhil Bureau 2604 Hai Essalam, Ville Nouvelle
Karim.BELLAHCENE@sahelreseau.com
www.SahelReseau.com
Logo with or without the Map

```html
<!DOCTYPE html>
<html lang="fr">
<head>
<meta charset="utf-8">
<title>Les Sentiers Bleus – Stationery</title>
<link rel="stylesheet" href="https://fonts.googleapis.com/css2?family=Arimo:wght@400;700&display=swap">
<style>
:root{
  --green:#1e5b3d;
  --red:#b3202b;
  --paper:#ffffff;
  --ink:#333333;
  --muted:#8a8a8a;
  --rule:#c9c9c9;
  --stage:#e9e7e3;
  --faint:#eef2ef;
}
*{box-sizing:border-box;margin:0;padding:0}
html,body{width:1200px;height:607px;overflow:hidden;background:var(--stage)}
body{position:relative;font-family:"Arimo",Arial,sans-serif;color:var(--ink)}
.sheet,.card,.envelope{position:absolute;background:var(--paper);box-shadow:0 2px 6px rgba(0,0,0,.18);overflow:hidden}
.brand{position:absolute;display:flex;align-items:center;gap:5px;color:var(--green);font-weight:700;white-space:nowrap}
.brand-mark{display:inline-block;background:var(--red)}
.swoosh{position:absolute;left:0;bottom:0;width:100%}
.contact{position:absolute;font-style:normal;font-size:5.5px;line-height:8px;color:var(--ink);white-space:nowrap}
.web{position:absolute;color:#fff;font-size:6.5px;white-space:nowrap}

/* letterhead */
.letterhead{left:34px;top:79px;width:357px;height:478px}
.letterhead .brand{left:30px;top:26px;font-size:13px}
.letterhead .brand-mark{width:8px;height:8px}
.watermark-area{position:absolute;left:60px;top:150px;width:160px;height:200px;border-radius:40% 30% 35% 45%;background:radial-gradient(circle,var(--faint),rgba(238,242,239,0) 72%)}
.letterhead .contact{left:26px;top:412px}
.letterhead .web{right:18px;bottom:8px}

/* fax */
.fax{left:427px;top:79px;width:357px;height:478px}
.fax .brand{left:30px;top:26px;font-size:13px}
.fax .brand-mark{width:8px;height:8px}
.fax-title{position:absolute;left:28px;top:58px;font-size:22px;font-weight:400;letter-spacing:1px}
.fax-fields{position:absolute;left:28px;top:88px;width:305px;display:grid;grid-template-columns:1fr 1fr;column-gap:24px;row-gap:7px}
.fax-field{display:flex;align-items:flex-end;font-size:5.5px;color:var(--muted);border-bottom:1px solid var(--rule);height:11px}
.fax-checks{position:absolute;left:28px;top:166px;display:flex;gap:14px;font-size:5.5px;color:var(--muted);white-space:nowrap}
.fax-check{display:flex;align-items:center;gap:3px}
.fax-check::before{content:"";width:6px;height:6px;border:1px solid var(--muted)}
.fax .contact{left:26px;top:412px}
.fax .web{right:18px;bottom:8px}

/* cards */
.card{width:147px;height:66px}
.card-1{left:826px;top:115px}
.card-2{left:989px;top:115px}
.card-3{left:826px;top:223px}
.card-4{left:989px;top:223px}
.card .brand{left:9px;top:9px;font-size:7.5px;gap:3px}
.card .brand-mark{width:5px;height:5px}
.card-person{position:absolute;right:9px;top:24px;text-align:right;font-size:5px;line-height:7px}
.card-person strong{display:block;font-size:5.5px}
.card .web{right:8px;bottom:4px;font-size:4.5px}

/* envelope */
.envelope{left:814px;top:341px;width:324px;height:197px}
.envelope .brand{left:128px;top:26px;font-size:11px;color:#fff}
.envelope .brand-mark{width:7px;height:7px}
.envelope .contact{left:22px;top:108px}
</style>
</head>
<body>

<section class="sheet letterhead" aria-label="Letterhead">
  <div class="brand"><span class="brand-mark"></span>Les Sentiers Bleus</div>
  <div class="watermark-area" role="img" aria-label="Faint map decoration"></div>
  <address class="contact">
    Centre Commercial et d’Affaire Ennakhil Bureau 2604 Hai Essalam, Ville Nouvelle<br>
    Tel: +000 (0) 55 10 20 30 &nbsp; Fax: +000 (0) 55 10 20 31<br>
    Karim.BELLAHCENE@sahelreseau.com
  </address>
  <svg class="swoosh" viewBox="0 0 357 44" height="44" preserveAspectRatio="none" aria-hidden="true">
    <path d="M0 30 C120 18 230 10 357 2 L357 44 L0 44Z" fill="var(--red)"/>
    <path d="M0 36 C120 24 230 16 357 8 L357 44 L0 44Z" fill="var(--green)"/>
  </svg>
  <div class="web">www.SahelReseau.com</div>
</section>

<section class="sheet fax" aria-label="Fax sheet">
  <div class="brand"><span class="brand-mark"></span>Les Sentiers Bleus</div>
  <h1 class="fax-title">FAX</h1>
  <div class="fax-fields">
    <div class="fax-field">To</div><div class="fax-field">From</div>
    <div class="fax-field">Fax</div><div class="fax-field">Pages</div>
    <div class="fax-field">Phone</div><div class="fax-field">Date</div>
    <div class="fax-field">Re</div><div class="fax-field">CC</div>
  </div>
  <div class="fax-checks">
    <span class="fax-check">Urgent</span>
    <span class="fax-check">For Review</span>
    <span class="fax-check">Please Comment</span>
    <span class="fax-check">Please Reply</span>
    <span class="fax-check">Please Recycle</span>
  </div>
  <address class="contact">
    Centre Commercial et d’Affaire Ennakhil Bureau 2604 Hai Essalam, Ville Nouvelle<br>
    Tel: +000 (0) 55 10 20 30 &nbsp; Fax: +000 (0) 55 10 20 31<br>
    Karim.BELLAHCENE@sahelreseau.com
  </address>
  <svg class="swoosh" viewBox="0 0 357 44" height="44" preserveAspectRatio="none" aria-hidden="true">
    <path d="M0 30 C120 18 230 10 357 2 L357 44 L0 44Z" fill="var(--red)"/>
    <path d="M0 36 C120 24 230 16 357 8 L357 44 L0 44Z" fill="var(--green)"/>
  </svg>
  <div class="web">www.SahelReseau.com</div>
</section>

<article class="card card-1" aria-label="Business card">
  <div class="brand"><span class="brand-mark"></span>Les Sentiers Bleus</div>
  <div class="card-person"><strong>Karim BELLAHCENE</strong>Directeur Générale</div>
  <svg class="swoosh" viewBox="0 0 147 20" height="20" preserveAspectRatio="none" aria-hidden="true">
    <path d="M0 8 C50 2 100 4 147 0 L147 20 L0 20Z" fill="var(--red)"/>
    <path d="M0 11 C50 5 100 7 147 3 L147 20 L0 20Z" fill="var(--green)"/>
  </svg>
  <div class="web">www.SahelReseau.com</div>
</article>

<article class="card card-2" aria-label="Business card">
  <div class="brand"><span class="brand-mark"></span>Les Sentiers Bleus</div>
  <div class="card-person"><strong>Karim BELLAHCENE</strong>Directeur Générale</div>
  <svg class="swoosh" viewBox="0 0 147 20" height="20" preserveAspectRatio="none" aria-hidden="true">
    <path d="M0 8 C50 2 100 4 147 0 L147 20 L0 20Z" fill="var(--red)"/>
    <path d="M0 11 C50 5 100 7 147 3 L147 20 L0 20Z" fill="var(--green)"/>
  </svg>
  <div class="web">www.SahelReseau.com</div>
</article>

<article class="card card-3" aria-label="Business card">
  <div class="brand"><span class="brand-mark"></span>Les Sentiers Bleus</div>
  <div class="card-person"><strong>Karim BELLAHCENE</strong>Directeur Générale</div>
  <svg class="swoosh" viewBox="0 0 147 20" height="20" preserveAspectRatio="none" aria-hidden="true">
    <path d="M0 8 C50 2 100 4 147 0 L147 20 L0 20Z" fill="var(--red)"/>
    <path d="M0 11 C50 5 100 7 147 3 L147 20 L0 20Z" fill="var(--green)"/>
  </svg>
  <div class="web">www.SahelReseau.com</div>
</article>

<article class="card card-4" aria-label="Business card">
  <div class="brand"><span class="brand-mark"></span>Les Sentiers Bleus</div>
  <div class="card-person"><strong>Karim BELLAHCENE</strong>Directeur Générale</div>
  <svg class="swoosh" viewBox="0 0 147 20" height="20" preserveAspectRatio="none" aria-hidden="true">
    <path d="M0 8 C50 2 100 4 147 0 L147 20 L0 20Z" fill="var(--red)"/>
    <path d="M0 11 C50 5 100 7 147 3 L147 20 L0 20Z" fill="var(--green)"/>
  </svg>
  <div class="web">www.SahelReseau.com</div>
</article>

<section class="envelope" aria-label="Envelope">
  <svg class="swoosh" style="top:0;bottom:auto" viewBox="0 0 324 90" height="90" preserveAspectRatio="none" aria-hidden="true">
    <path d="M0 0 L324 0 L324 40 C230 76 100 80 0 46Z" fill="var(--red)"/>
    <path d="M0 0 L324 0 L324 35 C230 71 100 75 0 41Z" fill="var(--green)"/>
  </svg>
  <div class="brand"><span class="brand-mark"></span>Les Sentiers Bleus</div>
  <address class="contact">
    Centre Commercial et d’Affaire Ennakhil Bureau 2604<br>
    Hai Essalam, Ville Nouvelle
  </address>
</section>

</body>
</html>
```